Garden Design Flier

I would like a PDF of this half page A4 flier in soft green tones with dark green leaves.

Target Market(s)

Home owners and real estate agents

Font styles to use
Serif
Other font styles liked:
• Papyrus

Colors
acd136
9bcb3c
cadf82
fefdec

Requirements
Must have
• Green tones
Nice to have
• Leaves, vines, lawns
Should not have
• Open to ideas, but classic style

```html
<!DOCTYPE html>
<html lang="en">
<head>
<meta charset="utf-8">
<title>Fernlot Gardens – Garden Design Flier</title>
<link rel="stylesheet" href="https://fonts.googleapis.com/css2?family=Tinos:wght@400;700&family=Questrial&display=swap">
<style>
  :root {
    --sky-top: #3fc3b4;
    --sky-mid: #36b9a8;
    --teal-deep: #2fae9d;
    --lawn-light: #8fd33a;
    --lawn-mid: #5cb92c;
    --lawn-dark: #3d9c22;
    --band-light: #2aa62a;
    --band-mid: #22a322;
    --band-dark: #1a8a1c;
    --brand-green: #4a9e1e;
    --byline-green: #2c9a1f;
    --text-white: #ffffff;
    --icon-green: #1e9a3a;
  }
  * { margin: 0; padding: 0; box-sizing: border-box; }
  html, body { width: 849px; height: 1200px; overflow: hidden; }
  body { background: var(--sky-mid); }

  .flier {
    position: relative;
    width: 849px;
    height: 1200px;
    overflow: hidden;
    font-family: "Tinos", "Times New Roman", serif;
  }

  .backdrop { position: absolute; inset: 0; }

  .brand {
    position: absolute;
    left: 60px;
    top: 30px;
    width: 700px;
    color: var(--brand-green);
    font-family: "Tinos", "Times New Roman", serif;
    font-weight: 700;
  }
  .brand-mark {
    position: absolute;
    left: 0;
    top: 44px;
    width: 30px;
    height: 30px;
    border-radius: 50%;
    background: var(--brand-green);
  }
  .brand-name {
    position: absolute;
    left: 40px;
    top: 0;
    font-size: 140px;
    line-height: 1;
    letter-spacing: 6px;
  }
  .brand-sub {
    position: absolute;
    right: -6px;
    top: 110px;
    font-size: 34px;
    letter-spacing: 10px;
    line-height: 1;
  }

  .byline {
    position: absolute;
    left: 0;
    width: 818px;
    text-align: center;
    font-family: "Questrial", "Century Gothic", sans-serif;
    color: var(--byline-green);
    text-shadow: 0 0 3px rgba(255,255,255,0.8);
    font-weight: 700;
  }
  .byline-name { top: 176px; font-size: 27px; }
  .byline-cert { top: 215px; font-size: 27px; }

  .services { position: absolute; left: 0; top: 0; }

  .pitch {
    position: absolute;
    left: 0;
    top: 846px;
    width: 849px;
    text-align: center;
    color: var(--text-white);
    font-weight: 700;
    font-size: 33px;
    line-height: 44px;
    text-shadow: 2px 2px 3px rgba(0,0,0,0.55);
  }
  .pitch p + p { margin-top: 2px; }

  .contact {
    position: absolute;
    top: 1119px;
    left: 0;
    width: 849px;
    height: 42px;
  }
  .contact-item {
    position: absolute;
    top: 0;
    display: flex;
    align-items: center;
    gap: 14px;
    color: var(--text-white);
    font-weight: 700;
    font-size: 22px;
    text-shadow: 1px 1px 2px rgba(0,0,0,0.5);
  }
  .contact-icon {
    width: 42px;
    height: 42px;
    border-radius: 50%;
    background: var(--icon-green);
    display: flex;
    align-items: center;
    justify-content: center;
    flex: none;
  }
  .contact-email { left: 14px; }
  .contact-phone { left: 410px; }
  .contact-abn { left: 644px; }
</style>
</head>
<body>
<main class="flier">

  <svg class="backdrop" width="849" height="1200" viewBox="0 0 849 1200" role="img" aria-label="Soft teal sky with drifting clouds and leaves above a sunlit green lawn">
    <defs>
      <linearGradient id="sky" x1="0" y1="0" x2="0" y2="1">
        <stop offset="0" stop-color="var(--sky-top)"/>
        <stop offset="0.3" stop-color="#6fd0c2"/>
        <stop offset="0.45" stop-color="var(--sky-mid)"/>
        <stop offset="1" stop-color="var(--teal-deep)"/>
      </linearGradient>
      <linearGradient id="lawn" x1="0" y1="0" x2="0" y2="1">
        <stop offset="0" stop-color="var(--lawn-light)"/>
        <stop offset="0.45" stop-color="var(--lawn-mid)"/>
        <stop offset="1" stop-color="var(--lawn-dark)"/>
      </linearGradient>
    </defs>
    <rect width="849" height="1200" fill="url(#sky)"/>
    <path d="M0 890 C 200 880 420 935 849 925 L 849 1200 L 0 1200 Z" fill="url(#lawn)"/>
  </svg>

  <header class="brand" aria-label="Fernlot Gardens">
    <span class="brand-mark"></span>
    <span class="brand-name">FERNLOT</span>
    <span class="brand-sub">GARDENS</span>
  </header>

  <p class="byline byline-name">by: Liam Harrow</p>
  <p class="byline byline-cert">Certificate 3. Horticulture. Westbrook Institute</p>

  <svg class="services" width="849" height="1200" viewBox="0 0 849 1200" aria-label="Design, install, grow, tend, enjoy">
    <polygon class="band band-design" points="46.5,361 803,265 803,366 46.5,463" fill="var(--band-light)"/>
    <polygon class="band band-grow" points="50,489 803,389 803,490 50,588" fill="var(--band-mid)" opacity="0.92"/>
    <polygon class="band band-enjoy" points="46.5,625 803,527 803,667 46.5,763" fill="var(--band-dark)"/>
    <g fill="var(--text-white)" font-family="Tinos, 'Times New Roman', serif" font-weight="700" style="filter: drop-shadow(2px 3px 2px rgba(0,0,0,0.45))">
      <text transform="translate(85,428) rotate(-7.36)" font-size="84" textLength="716" lengthAdjust="spacingAndGlyphs">DESIGN • INSTALL</text>
      <text transform="translate(137,548) rotate(-7.36)" font-size="100" textLength="582" lengthAdjust="spacingAndGlyphs">GROW • TEND</text>
      <text transform="translate(188,718) rotate(-7.36)" font-size="150" textLength="485" lengthAdjust="spacingAndGlyphs">ENJOY</text>
    </g>
  </svg>

  <section class="pitch">
    <p>All your gardening needs from design and<br>installation to general maintenance</p>
    <p>Bespoke vegetable gardens and potager designs<br>created to suit your site and requirements</p>
  </section>

  <footer class="contact">
    <div class="contact-item contact-email">
      <span class="contact-icon">
        <svg width="26" height="18" viewBox="0 0 26 18"><rect x="1" y="1" width="24" height="16" fill="none" stroke="#fff" stroke-width="2"/><path d="M1 1 L13 10 L25 1 M1 17 L10 8 M25 17 L16 8" fill="none" stroke="#fff" stroke-width="2"/></svg>
      </span>
      <span>liam@fernlotgardens.com.au</span>
    </div>
    <div class="contact-item contact-phone">
      <span class="contact-icon">
        <svg width="16" height="26" viewBox="0 0 16 26"><rect x="1" y="1" width="14" height="24" rx="2" fill="none" stroke="#fff" stroke-width="2"/><line x1="1" y1="20" x2="15" y2="20" stroke="#fff" stroke-width="1.5"/><circle cx="8" cy="22.5" r="1.2" fill="#fff"/></svg>
      </span>
      <span>0400-183527</span>
    </div>
    <div class="contact-item contact-abn">
      <span class="contact-icon"></span>
      <span>51203964718</span>
    </div>
  </footer>

</main>
</body>
</html>
```